Domestic violence resource cards for distribution to at-risk patients in an emergency department

Using the attached image(or very similar) and text document, a tri-fold business card is requested that integrates the image on the outside and the document content throughout the card's remaining faces. A creative format is requested, one that does not look like the typical cold, uncaring bullet point outlines that are found in similar resource projects. Bold or larger font sizes are requested for headings and body text is not required to be aligned or justified and the bullet points in the supplied document can be removed for creative license. Palattes should be clear, avoiding neons or implied target gender. Legibility is paramount, but again a creative presentation of a very serious subject is our goal. These cards are intended to be distributed to patients or others in the emergency department that may benefit from domestic violence resources. The business card size is mandatory so that the card can be concealed if needed by the receiver.
Updates

Reason: There are several revisions from designers that we are anxiously awaiting; we want to provide time for these designers to submit new designs but also continue spending time with their families and friends around the holiday season.

Target Market(s)

Patients and family in contact with emergency services

Industry/Entity Type

Healthcare

Contact Information for Business Card

Double sided tri-fold card with image on outer sides, text content and resource phone numbers on the exterior. When complete, the card should fold to standard US business card size.

Font styles to use
Other font styles liked:
• Designer's choice, but clear and legible

Requirements
Must have
• See above description. Card must be tri-fold, fold down to standard business card size, remain easily readable, and fold along the long edge.
Should not have
• Cartoon images; bloated fonts or clipart; bright, flashy neon or rainbow-like colors; additional graphics or charts.

```html
<!DOCTYPE html>
<html lang="en">
<head>
<meta charset="utf-8">
<title>Always remember – Safety planning card</title>
<link href="https://fonts.googleapis.com/css2?family=Cabin:ital,wght@0,400;0,600;0,700;1,400&family=Fira+Sans:wght@400;600&display=swap" rel="stylesheet">
<style>
  :root {
    --plum: #5f1a4e;
    --ink: #1c1c1c;
    --paper: #ffffff;
    --rule: #8a8a8a;
  }
  * { margin: 0; padding: 0; box-sizing: border-box; }
  html, body { width: 720px; height: 1200px; overflow: hidden; background: var(--paper); }
  .card {
    position: relative;
    width: 720px;
    height: 1200px;
    background: var(--paper);
    color: var(--ink);
    font-family: "Cabin", sans-serif;
  }
  .band {
    position: absolute;
    left: 0;
    width: 720px;
    background: var(--plum);
    color: var(--paper);
    font-family: "Cabin", sans-serif;
    font-weight: 600;
  }
  .band--top { top: 0; height: 106px; }
  .band--top h1 {
    position: absolute;
    left: 46px;
    top: 34px;
    font-size: 29px;
    font-weight: 600;
    letter-spacing: 0.5px;
  }
  .band--plan { top: 408px; height: 82px; }
  .band--plan h2 {
    position: absolute;
    left: 42px;
    top: 11px;
    font-size: 24px;
    font-weight: 600;
    line-height: 30px;
    letter-spacing: 0.4px;
  }
  .affirm { position: absolute; line-height: 1.2; }
  .affirm--alone {
    left: 53px; top: 112px;
    font-size: 38px;
    font-variant: small-caps;
    font-weight: 400;
  }
  .affirm--alone u { text-underline-offset: 4px; text-decoration-thickness: 1.5px; }
  .affirm--safe {
    left: 401px; top: 136px;
    font-size: 21.5px;
    line-height: 28px;
  }
  .affirm--protect {
    left: 40px; top: 178px;
    width: 260px;
    font-size: 18px;
    font-style: italic;
    text-align: center;
    line-height: 25px;
  }
  .affirm--children {
    left: 340px; top: 206px;
    font-size: 25.5px;
    line-height: 34px;
  }
  .affirm--hit {
    left: 66px; top: 289px;
    font-size: 20.5px;
    line-height: 26px;
  }
  .affirm--hit b { font-weight: 700; }
  .affirm--choices {
    left: 365px; top: 342px;
    font-size: 32px;
    font-weight: 700;
    letter-spacing: 0.3px;
  }
  .tips {
    position: absolute;
    left: 66px;
    width: 620px;
    list-style: none;
    font-family: "Fira Sans", sans-serif;
    font-size: 19.5px;
    line-height: 23.7px;
  }
  .tips--home { top: 514px; }
  .tips--away { top: 802px; }
  .tips li { position: relative; padding-left: 24px; }
  .tips li::before {
    content: "";
    position: absolute;
    left: 0; top: 6px;
    width: 0; height: 0;
    border-top: 6px solid transparent;
    border-bottom: 6px solid transparent;
    border-left: 11px solid var(--ink);
  }
  .tips li::after {
    content: "";
    position: absolute;
    left: 2px; top: 9px;
    width: 0; height: 0;
    border-top: 3px solid transparent;
    border-bottom: 3px solid transparent;
    border-left: 5.5px solid var(--paper);
  }
  .tips b { font-weight: 600; }
  .fold-line {
    position: absolute;
    left: 0; top: 798px;
    width: 720px;
    border: 0;
    border-top: 1.5px dashed var(--rule);
  }
</style>
</head>
<body>
<main class="card">
  <header class="band band--top"><h1>Always remember...</h1></header>

  <p class="affirm affirm--alone">You are <u>not alone</u>.</p>
  <p class="affirm affirm--safe">You have a right to be<br>safe anywhere.</p>
  <p class="affirm affirm--protect">You have a right to protect you or your children until you are out of danger.</p>
  <p class="affirm affirm--children">Your children deserve to<br>grow up without violence.</p>
  <p class="affirm affirm--hit">You <b>don’t</b> deserve to be hit<br>or threatened.</p>
  <p class="affirm affirm--choices">You have choices.</p>

  <section class="band band--plan">
    <h2>Leaving can be tough and very dangerous.<br>Here are some tips to help you plan for safety:</h2>
  </section>

  <ul class="tips tips--home">
    <li><b>Know people you can talk to</b> and ask them to call the<br>police if they hear a disturbance coming from your home</li>
    <li><b>Teach your children</b> how to contact the police or fire<br>department</li>
    <li><b>Practice</b> how to get you and your children out of your<br>home quickly and safely</li>
    <li><b>Plan</b> where you will go if you have to leave right away<br>and know the location of local emergency shelters</li>
    <li><b>Leave copies</b> of important papers, keys, cash, IDs, and<br>medicine with a friend or relative you trust</li>
    <li><b>Have a small bag packed</b> and ready at a friend or<br>relative’s house so you can leave quick</li>
  </ul>

  <hr class="fold-line">

  <ul class="tips tips--away">
    <li><b>Stay off social media</b> or cancel you accounts so that<br>you can’t be found online or through your friends</li>
    <li><b>Do not talk about your plans</b> in public areas or in mixed<br>groups</li>
    <li><b>Open a credit card or bank account</b> in your name only<br>and do not use it until you are ready</li>
    <li><b>Keep a charged prepaid cell phone</b> and a shelter<br>hotline number ready for emergencies</li>
    <li><b>Review your plan</b> often and only share with trusted<br>friends or family</li>
    <li><b>Be careful</b>: you are at most risk during the first 72 hours<br>after leaving an abusive situation</li>
    <li><b>Seek help</b> at a police station, firehouse or hospital if<br>needed</li>
  </ul>
</main>
</body>
</html>
```